Wine Label

I need a label for my home made red wine. I name it Kestravin Reserve, I want a vintage design with an "Ouroboros encircled around a Sowilo rune" incorporated in the design

```html
<!DOCTYPE html>
<html lang="en">
<head>
<meta charset="utf-8">
<title>Kestravin Reserve — Wine Label</title>
<link href="https://fonts.googleapis.com/css2?family=Metamorphous&family=Old+Standard+TT:wght@400;700&display=swap" rel="stylesheet">
<style>
  :root {
    --backdrop: #5f6475;
    --label-paper: #f4f3ef;
    --label-edge: #d9d8d3;
    --ink: #1c1c1c;
    --serpent-tone: #a9a8a3;
  }
  html, body {
    margin: 0;
    padding: 0;
    width: 1200px;
    height: 900px;
    overflow: hidden;
    background: var(--backdrop);
  }
  .canvas {
    width: 1200px;
    height: 900px;
    display: flex;
    align-items: center;
    justify-content: center;
  }
  .wine-label {
    width: 600px;
    height: 733px;
    display: block;
  }
  .label-paper { fill: var(--label-paper); stroke: var(--label-edge); stroke-width: 2; }
  .serpent-ring { fill: var(--serpent-tone); }
  .arc-title {
    font-family: "Metamorphous", serif;
    font-size: 36px;
    letter-spacing: 3px;
    fill: var(--ink);
    text-transform: uppercase;
  }
  .brand-name {
    font-family: "Metamorphous", serif;
    font-size: 38px;
    fill: var(--ink);
  }
  .side-note {
    font-family: "Old Standard TT", serif;
    font-size: 17px;
    fill: var(--ink);
    letter-spacing: 1px;
  }
  .divider-mark {
    font-family: "Old Standard TT", serif;
    font-size: 16px;
    fill: var(--ink);
  }
  .volume {
    font-family: "Old Standard TT", serif;
    font-size: 15px;
    fill: var(--ink);
  }
</style>
</head>
<body>
<main class="canvas">
  <svg class="wine-label" viewBox="0 0 540 660" xmlns="http://www.w3.org/2000/svg">
    <defs>
      <path id="arc-top" d="M 95 330 A 175 237 0 0 1 445 330"/>
      <path id="arc-bottom" d="M 70 330 A 200 262 0 0 0 470 330"/>
    </defs>

    <ellipse class="label-paper" cx="270" cy="330" rx="262" ry="322"/>

    <path class="serpent-ring" role="img" aria-label="Engraved ouroboros serpent coiled in a ring, biting its own tail"
          fill-rule="evenodd"
          d="M 30 330 A 240 300 0 1 0 510 330 A 240 300 0 1 0 30 330 Z
             M 58 330 A 212 272 0 1 1 482 330 A 212 272 0 1 1 58 330 Z"/>

    <text class="arc-title" text-anchor="middle">
      <textPath href="#arc-top" startOffset="50%">Kestravin Reserve</textPath>
    </text>
    <text class="arc-title" text-anchor="middle">
      <textPath href="#arc-bottom" startOffset="50%">Kestravin Reserve</textPath>
    </text>

    <text class="brand-name" x="270" y="345" text-anchor="middle">Kestravin</text>

    <g class="side-left">
      <text class="side-note" x="140" y="322" text-anchor="middle">HOME</text>
      <text class="side-note" x="140" y="344" text-anchor="middle">MADE</text>
      <text class="divider-mark" x="104" y="346" text-anchor="middle">×</text>
    </g>
    <g class="side-right">
      <text class="side-note" x="400" y="322" text-anchor="middle">RED</text>
      <text class="side-note" x="400" y="344" text-anchor="middle">WINE</text>
      <text class="divider-mark" x="436" y="346" text-anchor="middle">×</text>
    </g>

    <text class="volume" x="270" y="470" text-anchor="middle">700ml</text>
  </svg>
</main>
</body>
</html>
```